Label Design Project

I will need 3 different labels:Using the Rosalind Outreach Ventures logo on the front of each with different names of the jams on each. One label should indicate Honey On My Muffin Spiced Plum Jam, One label should be Plum Good Morning and one label for Larkfield Toffee. I would like for the label to wrap around and not 2 separate labels. except for the Larkfield Toffee. This label should have portrait layout or two labels with the name of the Larkfield Toffee on the front and the story and nutritional label on back. Jar dimensions for the label: W 2-3/4" x H 3-5/8 and L 8" Each Jam label should have the Outreach story, Nutrition, and a logo. The nuts label will have the logo with the name of the nut (Larkfield Toffee) on the front and story, nutritional label and ingredients on the back. This label should be W 2 1/2" and L 3". I've attached a sample of what I have however, the text is too small.

```html
<!DOCTYPE html>
<html lang="en">
<head>
<meta charset="utf-8">
<title>Rosalind Outreach Ventures – Jar &amp; Bag Labels</title>
<link href="https://fonts.googleapis.com/css2?family=PT+Sans:ital,wght@0,700;1,700&family=Roboto+Condensed:wght@700&family=Libre+Franklin:wght@400;700;900&display=swap" rel="stylesheet">
<style>
  :root {
    --maroon: #7b1d22;
    --maroon-dark: #6a1a1e;
    --peach-light: #fde9d4;
    --peach: #f9cfae;
    --blush: #f7c4bd;
    --cream: #fff6ea;
    --white: #ffffff;
    --ink: #111111;
    --fruit-red: #d8502f;
    --fruit-gold: #f3a93a;
    --leaf: #3f7a2a;
  }
  * { box-sizing: border-box; margin: 0; padding: 0; }
  html, body { width: 1169px; height: 1200px; overflow: hidden; background: var(--white); }
  body { position: relative; font-family: "PT Sans", sans-serif; color: var(--maroon); }

  .label {
    position: absolute;
    background:
      radial-gradient(ellipse at 45% 40%, rgba(255,255,255,.75), rgba(255,255,255,0) 55%),
      linear-gradient(100deg, var(--blush) 0%, var(--peach-light) 45%, var(--peach) 75%, var(--cream) 100%);
    box-shadow: 0 1px 5px rgba(0,0,0,.25);
  }
  .label::before {
    content: ""; position: absolute; inset: 8px;
    border: 3px solid var(--maroon);
  }
  .label--thin::before { border-width: 1px; inset: 7px; }

  .label--wrap { left: 58px; width: 1043px; height: 305px; }
  .label--wrap.one { top: 42px; }
  .label--wrap.two { top: 377px; }

  .story {
    position: absolute; text-align: center; font-weight: 700;
    font-size: 12.6px; line-height: 13.6px;
  }
  .story p { margin-bottom: 13px; }
  .story .verse { font-style: italic; }
  .story .web { margin-bottom: 0; }
  .label--wrap .story { left: 22px; top: 40px; width: 290px; }

  .brand {
    position: absolute; text-align: center;
    font-family: "PT Sans", sans-serif; font-weight: 700; color: var(--maroon);
    display: flex; flex-direction: column; align-items: center; justify-content: center; gap: 8px;
  }
  .brand .dot { width: 16px; height: 16px; border-radius: 50%; background: var(--maroon); }
  .label--wrap .brand { left: 400px; top: 48px; width: 290px; height: 150px; font-size: 30px; line-height: 32px; }

  .fruit { position: absolute; border-radius: 50%; }
  .fruit--left {
    left: 318px; top: 150px; width: 112px; height: 92px;
    background: radial-gradient(circle at 35% 45%, var(--fruit-gold), var(--fruit-red) 70%, var(--leaf) 100%);
  }
  .fruit--right {
    left: 700px; top: 130px; width: 100px; height: 100px;
    background: radial-gradient(circle at 60% 40%, var(--fruit-gold), var(--fruit-red) 75%, var(--leaf) 100%);
  }

  .jam-name {
    position: absolute; left: 330px; width: 420px; top: 248px; text-align: center;
    font-family: "Roboto Condensed", sans-serif; font-weight: 700; font-size: 29px; color: var(--maroon-dark);
    white-space: nowrap;
  }
  .two .jam-name { font-size: 33px; top: 244px; }

  .nutrition {
    position: absolute; background: var(--white); border: 1px solid var(--ink);
    color: var(--ink); font-family: "Libre Franklin", sans-serif; padding: 3px 4px;
  }
  .label--wrap .nutrition { left: 802px; top: 36px; width: 178px; height: 240px; font-size: 7px; line-height: 1; }
  .nutrition h3 { font-weight: 900; font-size: 20px; line-height: 20px; }
  .nutrition .row { display: flex; justify-content: space-between; padding: 2.2px 0; border-top: 1px solid var(--ink); }
  .nutrition .row.indent { padding-left: 8px; }
  .nutrition .bar-thick { border-top: 7px solid var(--ink); }
  .nutrition .bar-mid { border-top: 3px solid var(--ink); }
  .nutrition b { font-weight: 700; }
  .nutrition .foot { font-size: 5.5px; padding-top: 3px; border-top: 1px solid var(--ink); }

  .label--front { left: 204px; top: 714px; width: 364px; height: 398px; }
  .label--front .brand { left: 40px; top: 50px; width: 284px; height: 170px; font-size: 32px; line-height: 34px; }
  .label--front .bag-name {
    position: absolute; left: 0; width: 100%; top: 262px; text-align: center;
    font-family: "Roboto Condensed", sans-serif; font-weight: 700; font-size: 51px; line-height: 54px; color: var(--maroon-dark);
  }

  .label--back { left: 595px; top: 714px; width: 365px; height: 398px; }
  .label--back .nutrition {
    left: 26px; top: 23px; width: 313px; height: 95px; font-size: 6px; line-height: 1; padding: 3px;
    display: grid; grid-template-columns: 84px 1fr 1fr; column-gap: 6px;
  }
  .label--back .nutrition h3 { font-size: 14px; line-height: 13px; }
  .label--back .col .row { padding: 1.6px 0; }
  .label--back .lead { font-size: 5.5px; }
  .label--back .lead .cal { font-size: 10px; font-weight: 900; display: flex; justify-content: space-between; border-top: 4px solid var(--ink); padding-top: 2px; margin-top: 2px; }
  .label--back .extras { grid-column: 2 / 4; font-size: 5.5px; border-top: 3px solid var(--ink); padding-top: 2px; }
  .label--back .ingredients { grid-column: 1 / 4; font-size: 5.5px; border-top: 1px solid var(--ink); padding-top: 2px; }
  .label--back .story { left: 20px; top: 150px; width: 325px; }
</style>
</head>
<body>

  <section class="label label--wrap one" aria-label="Honey On My Muffin Spiced Plum Jam wrap label">
    <div class="story">
      <p>Thank you! The product you just purchased is hand-crafted from the finest ingredients and packaged with loving care by friends of Rosalind Outreach. Your purchase supports the Outreach's Social Enterprise Programs, which provide poverty-stricken families in the Deep South with the skills and opportunities to work their way from poverty to independance.</p>
      <p>Please accept our deepest thanks for your support!</p>
      <p class="verse">You shall freely open your hand to your brother, to your needy and poor in your land. - Deuteronomy 15:11</p>
      <p class="web">www.rosalindoutreach.org</p>
    </div>
    <div class="fruit fruit--left" role="img" aria-label="Photo of fresh plums with leaves"></div>
    <div class="fruit fruit--right" role="img" aria-label="Photo of whole plums with a leaf"></div>
    <div class="brand"><span class="dot"></span><span>Rosalind Outreach Ventures</span></div>
    <h2 class="jam-name">Honey On My Muffin Spiced Plum Jam</h2>
    <div class="nutrition">
      <h3>Nutrition Facts</h3>
      <div>Serving Size: 1 tbsp (20g)<br>Servings Per Container: 16</div>
      <div class="row bar-thick"><b>Amount Per Serving</b></div>
      <div class="row"><span><b>Calories</b> 15</span><span>Calories from Fat 0</span></div>
      <div class="row bar-mid"><span></span><b>% Daily Value*</b></div>
      <div class="row"><span><b>Total Fat</b> 0g</span><b>0%</b></div>
      <div class="row indent"><span>Saturated Fat 0g</span><b>0%</b></div>
      <div class="row indent"><i>Trans Fat 0g</i></div>
      <div class="row"><span><b>Cholesterol</b> 0mg</span><b>0%</b></div>
      <div class="row"><span><b>Sodium</b> 110mg</span><b>5%</b></div>
      <div class="row"><span><b>Total Carbohydrate</b> 4g</span><b>1%</b></div>
      <div class="row indent"><span>Dietary Fiber 0g</span><b>0%</b></div>
      <div class="row indent"><span>Sugars 4g</span></div>
      <div class="row"><span><b>Protein</b> 0g</span></div>
      <div class="row bar-thick"><span>Vitamin A 0%</span><span>•</span><span>Vitamin C 2%</span></div>
      <div class="row"><span>Calcium 0%</span><span>•</span><span>Iron 0%</span></div>
      <div class="foot">* Percent Daily Values are based on a 2,000 calorie diet.</div>
    </div>
  </section>

  <section class="label label--wrap two" aria-label="Plum Good Morning Jam wrap label">
    <div class="story">
      <p>Thank you! The product you just purchased is hand-crafted from the finest ingredients and packaged with loving care by friends of Rosalind Outreach. Your purchase supports the Outreach's Social Enterprise Programs, which provide poverty-stricken families in the Deep South with the skills and opportunities to work their way from poverty to independance.</p>
      <p>Please accept our deepest thanks for your support!</p>
      <p class="verse">You shall freely open your hand to your brother, to your needy and poor in your land. - Deuteronomy 15:11</p>
      <p class="web">www.rosalindoutreach.org</p>
    </div>
    <div class="fruit fruit--left" role="img" aria-label="Photo of fresh plums with leaves"></div>
    <div class="fruit fruit--right" role="img" aria-label="Photo of whole plums with a leaf"></div>
    <div class="brand"><span class="dot"></span><span>Rosalind Outreach Ventures</span></div>
    <h2 class="jam-name">Plum Good Morning Jam</h2>
    <div class="nutrition">
      <h3>Nutrition Facts</h3>
      <div>Serving Size: 1 tbsp (20g)<br>Servings Per Container: 16</div>
      <div class="row bar-thick"><b>Amount Per Serving</b></div>
      <div class="row"><span><b>Calories</b> 15</span><span>Calories from Fat 0</span></div>
      <div class="row bar-mid"><span></span><b>% Daily Value*</b></div>
      <div class="row"><span><b>Total Fat</b> 0g</span><b>0%</b></div>
      <div class="row indent"><span>Saturated Fat 0g</span><b>0%</b></div>
      <div class="row indent"><i>Trans Fat 0g</i></div>
      <div class="row"><span><b>Cholesterol</b> 0mg</span><b>0%</b></div>
      <div class="row"><span><b>Sodium</b> 110mg</span><b>5%</b></div>
      <div class="row"><span><b>Total Carbohydrate</b> 4g</span><b>1%</b></div>
      <div class="row indent"><span>Dietary Fiber 0g</span><b>0%</b></div>
      <div class="row indent"><span>Sugars 4g</span></div>
      <div class="row"><span><b>Protein</b> 0g</span></div>
      <div class="row bar-thick"><span>Vitamin A 0%</span><span>•</span><span>Vitamin C 2%</span></div>
      <div class="row"><span>Calcium 0%</span><span>•</span><span>Iron 0%</span></div>
      <div class="foot">* Percent Daily Values are based on a 2,000 calorie diet.</div>
    </div>
  </section>

  <section class="label label--thin label--front" aria-label="Larkfield Toffee front label">
    <div class="brand"><span class="dot"></span><span>Rosalind Outreach Ventures</span></div>
    <h2 class="bag-name">Larkfield<br>Toffee</h2>
  </section>

  <section class="label label--thin label--back" aria-label="Larkfield Toffee back label">
    <div class="nutrition">
      <div class="lead">
        <h3>Nutrition Facts</h3>
        <div style="margin-top:4px">15 servings per container</div>
        <div><b>Serv. Size<br>1 Tbs (17g)</b></div>
        <div class="cal"><span>Calories</span><span>30</span></div>
      </div>
      <div class="col">
        <div class="row"><b>Amount/Serving</b><b>% DV*</b></div>
        <div class="row bar-mid"><span><b>Total Fat</b> 0g</span><b>0%</b></div>
        <div class="row indent"><span>Sat. Fat 0g</span><b>0%</b></div>
        <div class="row indent"><i>Trans Fat 0g</i></div>
        <div class="row"><span><b>Cholest.</b> 0mg</span><b>0%</b></div>
        <div class="row"><span><b>Sodium</b> 0mg</span><b>0%</b></div>
      </div>
      <div class="col">
        <div class="row"><b>Amount/Serving</b><b>% DV*</b></div>
        <div class="row bar-mid"><span><b>Total Carb.</b> 7g</span><b>3%</b></div>
        <div class="row indent"><span>Fiber 0g</span><b>0%</b></div>
        <div class="row indent"><span>Total Sugars 7g</span></div>
        <div class="row indent"><span>Incl. 6g Added Sugars</span><b>12%</b></div>
        <div class="row"><span><b>Protein</b> 0g</span></div>
      </div>
      <div class="extras">Vitamin D 0mcg 0% • Calcium 0mg 0% • Iron 0mg 0%<br>Potassium 0mg 0% • Vitamin C 29mg 35%</div>
      <div class="ingredients">INGREDIENTS: Peaches, Sugar, Contains 2% or less of: Pectin, Citric Acid, Vitamin C</div>
    </div>
    <div class="story">
      <p>Thank you! The product you just purchased is hand-crafted from the finest ingredients and packaged with loving care by friends of Rosalind Outreach. Your purchase supports the Outreach's Social Enterprise Programs, which provide poverty-stricken families in the Deep South with the skills and opportunities to work their way from poverty to independance.</p>
      <p>Please accept our deepest thanks for your support!</p>
      <p class="verse">You shall freely open your hand to your brother, to your needy and poor in your land. - Deuteronomy 15:11</p>
      <p class="web">www.rosalindoutreach.org</p>
    </div>
  </section>

</body>
</html>
```